Reed & Vale NC grand opening (for BILLBOARD)

Advertising the grand opening of our cannabis/hemp shop in NC. We will sell all things hemp (flower, cartridges, disposables, edibles, creams, lotions, pet products etc...)

Requirements
Must have
• include, open starting Aug 1, but grand opening Aug 15th.
Nice to have
• Difference slogan ideas "Save some cash, buy our grass" "Find your perfect high at Reed & Vale cannabis store" "Experience Nature's Gift: Reed & Vale Cannabis Store"

```html
<!DOCTYPE html>
<html lang="en">
<head>
<meta charset="UTF-8">
<title>Reed &amp; Vale — Grand Opening Billboard</title>
<link href="https://fonts.googleapis.com/css2?family=Montserrat:wght@600;800;900&display=swap" rel="stylesheet">
<style>
  :root {
    --backdrop: #e3e9ef;
    --board: #f7f7f5;
    --forest: #04663a;
    --lime: #7cbe3f;
    --ink: #fbfbf8;
  }
  * { box-sizing: border-box; margin: 0; padding: 0; }
  html, body {
    width: 1200px;
    height: 900px;
    overflow: hidden;
    background: var(--backdrop);
  }
  .billboard {
    position: absolute;
    left: 40px;
    top: 206px;
    width: 1120px;
    height: 488px;
    background: var(--board);
    overflow: hidden;
    font-family: "Montserrat", sans-serif;
    box-shadow: 0 6px 24px rgba(0, 0, 0, 0.12);
  }
  .brand {
    position: absolute;
    left: 430px;
    top: 62px;
    width: 520px;
    display: flex;
    align-items: center;
    justify-content: center;
    gap: 14px;
  }
  .brand-dot {
    width: 26px;
    height: 26px;
    border-radius: 50%;
    background: var(--forest);
  }
  .brand-name {
    font-weight: 800;
    font-size: 60px;
    letter-spacing: -1px;
    color: var(--forest);
    line-height: 1;
  }
  .headline-band {
    position: absolute;
    left: 280px;
    top: 162px;
    right: 0;
    height: 166px;
    background: var(--forest);
  }
  .headline {
    position: absolute;
    left: 430px;
    top: 174px;
    font-weight: 900;
    font-size: 64px;
    line-height: 74px;
    color: var(--ink);
    text-transform: uppercase;
    letter-spacing: 0.5px;
  }
  .headline .accent { color: var(--lime); }
  .hero-leaf {
    position: absolute;
    left: 8px;
    top: 52px;
    width: 392px;
    height: 384px;
    border-radius: 46% 46% 40% 40%;
    background: radial-gradient(circle at 55% 60%, var(--lime) 0%, #3f9a3e 55%, var(--forest) 100%);
  }
  .location {
    position: absolute;
    left: 432px;
    top: 346px;
    display: flex;
    align-items: center;
    gap: 18px;
  }
  .location-pin { width: 34px; height: 48px; }
  .location-text {
    font-weight: 800;
    font-size: 36px;
    color: var(--forest);
    text-transform: uppercase;
    letter-spacing: 0.5px;
  }
  .opening-dates {
    position: absolute;
    left: 432px;
    top: 414px;
    font-weight: 800;
    font-size: 27px;
    line-height: 1.2;
    color: var(--forest);
    text-transform: uppercase;
    letter-spacing: 0.5px;
  }
  .opening-dates .accent { color: var(--lime); }
</style>
</head>
<body>
  <main class="billboard">
    <div class="brand">
      <span class="brand-dot"></span>
      <span class="brand-name">Reed &amp; Vale</span>
    </div>

    <div class="headline-band"></div>
    <h1 class="headline">
      Save some <span class="accent">cash,</span><br>
      Buy our <span class="accent">grass</span>
    </h1>

    <div class="hero-leaf" role="img" aria-label="Large two-tone green hemp leaf illustration"></div>

    <div class="location">
      <svg class="location-pin" viewBox="0 0 34 48" aria-hidden="true">
        <path d="M17 0C7.6 0 0 7.6 0 17c0 12 17 31 17 31s17-19 17-31C34 7.6 26.4 0 17 0z" fill="#7cbe3f"/>
        <circle cx="17" cy="17" r="8" fill="#f7f7f5"/>
      </svg>
      <span class="location-text">Exit 4B Maplebrook Rd</span>
    </div>

    <p class="opening-dates">Open Aug 1 · <span class="accent">Grand Opening Aug 15</span></p>
  </main>
</body>
</html>
```